Business Card design for law firm = Juriskite Australia

We are seeking a new design for our business cards.
We are keeping our logo, which is attached.
We need space for
Name
Title
Address is , which is
Level 14
82 Penhallow Street
Sydney NSW 2000
Phone :
Mobile :
Fax :
Email :
DX :
website www.juriskite.com.au

Industry/Entity Type

Law Firm / Banking and Finance

Contact Information for Business Card

We are seeking a new design for our business cards. We are keeping our logo. We need space for Name Title Address is Level 14 82 Penhallow Street Sydney NSW 2000 Phone Mobile Fax Email DX website www.juriskite.com.au

Colors
0054AA
0677BA
7BADD7
CADEEF
E8F1F8

Requirements
Must have
• see our website for general feel www.juriskite.com.au

```html
<!DOCTYPE html>
<html lang="en">
<head>
<meta charset="utf-8">
<title>Juriskite Australia – Business Card</title>
<link rel="stylesheet" href="https://fonts.googleapis.com/css2?family=Arimo:wght@400&family=Crimson+Text:wght@400&display=swap">
<style>
  :root {
    --stage: #2b2b2b;
    --card: #0c0c0c;
    --accent-blue: #1e90d6;
    --name-blue: #0a6fc0;
    --ink-light: #f4f4f4;
    --rule: #555555;
  }
  * { box-sizing: border-box; margin: 0; padding: 0; }
  html, body {
    width: 1200px; height: 900px; overflow: hidden;
    background: var(--stage);
  }
  .stage { position: relative; width: 1200px; height: 900px; }
  .card {
    position: absolute; left: 300px; width: 600px; height: 343px;
    background: var(--card);
    box-shadow: 0 10px 30px rgba(0,0,0,.55);
  }
  .card--front { top: 80px; }
  .card--back { top: 477px; }

  .wordmark {
    position: absolute;
    font-family: Arimo, sans-serif; font-weight: 400;
    font-size: 38px; line-height: 1; color: var(--ink-light);
  }
  .card--front .wordmark { left: 48px; top: 180px; width: 230px; }
  .card--back .wordmark { left: 0; right: 0; top: 128px; text-align: center; }

  .divider {
    position: absolute; left: 300px; top: 60px; width: 1px; height: 230px;
    background: var(--rule);
  }
  .contact {
    position: absolute; left: 330px; top: 52px; width: 250px;
    font-family: Arimo, sans-serif; color: var(--ink-light);
  }
  .contact__name {
    font-family: "Crimson Text", serif; font-size: 30px; line-height: 1;
    color: var(--name-blue);
  }
  .contact__title { font-size: 15px; color: var(--accent-blue); margin-top: 2px; }
  .contact__list { list-style: none; margin-top: 16px; }
  .contact__item {
    display: flex; align-items: center; gap: 10px;
    font-size: 15px; line-height: 25px; white-space: nowrap;
  }
  .contact__icon { width: 16px; height: 16px; flex: none; fill: var(--accent-blue); }
  .contact__web-name { color: var(--accent-blue); }
  .contact__address {
    font-style: normal; font-size: 16px; line-height: 22px; margin-top: 18px;
  }
  .dx {
    position: absolute; left: 0; right: 0; top: 215px; text-align: center;
    font-family: Arimo, sans-serif; font-size: 17px; color: var(--ink-light);
  }
  .dx__label { color: var(--accent-blue); }
</style>
</head>
<body>
<main class="stage">
  <section class="card card--front" aria-label="Business card front">
    <p class="wordmark">Juriskite</p>
    <div class="divider"></div>
    <div class="contact">
      <p class="contact__name">Daniel Harcourt</p>
      <p class="contact__title">Managing Director</p>
      <ul class="contact__list">
        <li class="contact__item">
          <svg class="contact__icon" viewBox="0 0 16 16" aria-label="Phone"><path d="M3 1l3 3-1.5 2a9 9 0 0 0 5.5 5.5L12 10l3 3-2 2C7 15 1 9 1 3z"/></svg>
          044-555 210 347
        </li>
        <li class="contact__item">
          <svg class="contact__icon" viewBox="0 0 16 16" aria-label="Mobile"><path d="M4 1h8v14H4zM5.5 2.5v9h5v-9z"/></svg>
          044-555 210 348
        </li>
        <li class="contact__item">
          <svg class="contact__icon" viewBox="0 0 16 16" aria-label="Fax"><path d="M4 1h8v4H4zM1 6h14v6h-3v3H4v-3H1zM5.5 10v3.5h5V10z"/></svg>
          044-555 210 349
        </li>
        <li class="contact__item">
          <svg class="contact__icon" viewBox="0 0 16 16" aria-label="Email"><path d="M1 3h14v10H1zM2.5 4.5 8 9l5.5-4.5z"/></svg>
          hello@juriskite.com.au
        </li>
        <li class="contact__item">
          <svg class="contact__icon" viewBox="0 0 16 16" aria-label="Website"><circle cx="8" cy="8" r="6.5" fill="none" stroke="var(--accent-blue)" stroke-width="1.5"/><path d="M1.5 8h13M8 1.5c-3 3.5-3 9.5 0 13M8 1.5c3 3.5 3 9.5 0 13" fill="none" stroke="var(--accent-blue)" stroke-width="1.2"/></svg>
          <span>www.<span class="contact__web-name">juriskite</span>.com.au</span>
        </li>
      </ul>
      <address class="contact__address">Level 14, 82 Penhallow Street<br>Sydney NSW 2000</address>
    </div>
  </section>

  <section class="card card--back" aria-label="Business card back">
    <p class="wordmark">Juriskite</p>
    <p class="dx"><span class="dx__label">DX :</span> 482715390</p>
  </section>
</main>
</body>
</html>
```